Snapframe Party Rentals New Business Card*

Need a business card designed for a Photo Booth Hire company.Must look very professional and colorful.A new creative logo would be a bonus. Our current logo is attached on here.

Contact Information for Business Card

Business Name: SNAPFRAME PARTY RENTALS
Contact Person: MARCUS OKAFOR
Mobile: 0491826350
Email: INFO@SNAPFRAMERENTALS.EXAMPLE
Website: WWW.SNAPFRAMERENTALS.EXAMPLE
Facebook: WWW.FACEBOOK.COM/SNAPFRAME.PARTY.RNT

Font styles to use
Serif
Sans Serif
Script

Colors

Designer to choose colors to be used in the design.

Requirements
Must have
• Bonus if the colors match our website.

```html
<!DOCTYPE html>
<html lang="en">
<head>
<meta charset="utf-8">
<title>Snapframe Party Rentals – Business Card</title>
<link rel="stylesheet" href="https://fonts.googleapis.com/css2?family=Cinzel:wght@400&family=Roboto:wght@400&family=Roboto+Condensed:wght@700&display=swap">
<style>
  :root {
    --backdrop: #8c8c8c;
    --card-dark: #141414;
    --card-light: #ffffff;
    --silver: #cfcfcf;
    --ink: #111111;
    --ink-soft: #6a6a6a;
    --rule: #9a9a9a;
  }
  * { margin: 0; padding: 0; box-sizing: border-box; }
  html, body {
    width: 1200px; height: 960px; overflow: hidden;
    background: var(--backdrop);
  }
  .canvas { position: relative; width: 1200px; height: 960px; }

  .card {
    position: absolute;
    width: 620px; height: 354px;
    box-shadow: 0 10px 24px rgba(0,0,0,.28);
  }

  /* Front */
  .card-front {
    left: 110px; top: 100px;
    background: var(--card-dark);
    display: flex; flex-direction: column; justify-content: center; align-items: center;
  }
  .front-name {
    font-family: "Cinzel", serif;
    font-weight: 400;
    color: var(--silver);
    font-size: 40px;
    line-height: 1.12;
    letter-spacing: 2px;
    text-align: center;
  }
  .front-tagline {
    margin-top: 10px;
    font-family: "Roboto Condensed", sans-serif;
    font-weight: 700;
    color: var(--silver);
    font-size: 12.5px;
    letter-spacing: 1.4px;
  }

  /* Back */
  .card-back {
    left: 470px; top: 500px;
    background: var(--card-light);
    display: flex; align-items: center;
    padding: 0 40px 0 52px;
  }
  .brand-block {
    width: 200px;
    display: flex; flex-direction: column; align-items: center; text-align: center;
  }
  .brand-dot {
    width: 64px; height: 64px; border-radius: 50%;
    background: var(--ink);
    margin-bottom: 16px;
  }
  .brand-name {
    font-family: "Roboto Condensed", sans-serif;
    font-weight: 700;
    color: var(--ink);
    font-size: 21px;
    line-height: 1.02;
  }
  .brand-url {
    margin-top: 4px;
    font-family: "Roboto Condensed", sans-serif;
    font-weight: 700;
    color: var(--ink);
    font-size: 9.5px;
    letter-spacing: .2px;
  }
  .divider {
    width: 1px; height: 150px;
    background: var(--rule);
    margin: 0 26px 0 22px;
  }
  .contact-block { flex: 1; }
  .person-name {
    font-family: "Roboto Condensed", sans-serif;
    font-weight: 700;
    color: var(--ink);
    font-size: 25px;
    letter-spacing: .5px;
    margin-bottom: 12px;
  }
  .contact-list { list-style: none; }
  .contact-item {
    display: flex; align-items: center; gap: 10px;
    font-family: "Roboto", sans-serif;
    font-size: 15px;
    color: var(--ink-soft);
    line-height: 22px;
  }
  .contact-icon { width: 12px; height: 12px; flex: none; }
</style>
</head>
<body>
<main class="canvas">

  <section class="card card-front" aria-label="Card front">
    <h1 class="front-name">SNAPFRAME<br>PARTY RENTALS</h1>
    <p class="front-tagline">MELBOURNE'S MOST AFFORDABLE PARTY RENTAL COMPANY</p>
  </section>

  <section class="card card-back" aria-label="Card back">
    <div class="brand-block">
      <span class="brand-dot" aria-hidden="true"></span>
      <p class="brand-name">SNAPFRAME<br>PARTY RENTALS</p>
      <p class="brand-url">WWW.SNAPFRAMERENTALS.EXAMPLE</p>
    </div>

    <span class="divider" aria-hidden="true"></span>

    <div class="contact-block">
      <h2 class="person-name">MARCUS OKAFOR</h2>
      <ul class="contact-list">
        <li class="contact-item">
          <svg class="contact-icon" viewBox="0 0 12 12" aria-hidden="true"><path fill="#111" d="M2.4 1l2 2.2-1 1.2c.7 1.5 1.8 2.6 3.3 3.3l1.2-1 2.1 2-1.1 1.9C5.1 10.4 1.6 6.9 1 2.1z"/></svg>
          0491826350
        </li>
        <li class="contact-item">
          <svg class="contact-icon" viewBox="0 0 12 12" aria-hidden="true"><rect x="0.5" y="2.5" width="11" height="7.5" fill="#111"/><path d="M1 3l5 3.6L11 3" stroke="#fff" stroke-width="1" fill="none"/></svg>
          info@snapframerentals.example
        </li>
        <li class="contact-item">
          <svg class="contact-icon" viewBox="0 0 12 12" aria-hidden="true"><circle cx="6" cy="6" r="5.5" fill="#111"/><path d="M.8 6h10.4M6 .6c-2.6 3-2.6 7.8 0 10.8M6 .6c2.6 3 2.6 7.8 0 10.8" stroke="#fff" stroke-width=".8" fill="none"/></svg>
          www.snapframerentals.example
        </li>
        <li class="contact-item">
          <svg class="contact-icon" viewBox="0 0 12 12" aria-hidden="true"><circle cx="6" cy="6" r="5.5" fill="#111"/></svg>
          /snapframe.party.rnt
        </li>
      </ul>
    </div>
  </section>

</main>
</body>
</html>
```